Tallow Crest Business Card

We need a business card designed for a a company called "Tallow Crest". We offer consulting, coaching and training to business leaders and coaches (across the world) using the latest findings in neuroscience, social and emotional intelligence and positive psychology. The final design should communicate the use of brain science to create sustainable relationships.

The card should be doublesided. The logo is attached and names and titles will be provided to the successful designer. Thank you.

Industry/Entity Type

Training

```html
<!DOCTYPE html>
<html lang="en">
<head>
<meta charset="utf-8">
<title>Tallow Crest Business Card</title>
<link href="https://fonts.googleapis.com/css2?family=Arimo:wght@400;700&display=swap" rel="stylesheet">
<style>
  :root {
    --teal: #00c6c7;
    --white: #ffffff;
    --edge: #8a8a8a;
    --faint: rgba(255, 255, 255, 0.4);
  }
  html, body {
    margin: 0;
    padding: 0;
    width: 847px;
    height: 1200px;
    overflow: hidden;
    background: var(--white);
  }
  body {
    position: relative;
    font-family: "Arimo", Arial, sans-serif;
  }
  .card {
    position: absolute;
    left: 1px;
    width: 845px;
    box-sizing: border-box;
    border-radius: 29px;
  }
  .card--front {
    top: 1px;
    height: 507px;
    border: 1.5px solid var(--edge);
    background: var(--white);
  }
  .card--back {
    top: 692px;
    height: 507px;
    background: var(--teal);
  }
  .holder-name {
    position: absolute;
    left: 70px;
    top: 86px;
    margin: 0;
    font-size: 39px;
    font-weight: 400;
    color: var(--teal);
    white-space: nowrap;
  }
  .holder-position {
    position: absolute;
    left: 71px;
    top: 140px;
    margin: 0;
    font-size: 21px;
    font-weight: 400;
    color: var(--teal);
    white-space: nowrap;
  }
  .contact-list {
    position: absolute;
    left: 64px;
    top: 268px;
    margin: 0;
    padding: 0;
    list-style: none;
    color: var(--teal);
    font-size: 24px;
  }
  .contact-item {
    position: relative;
    height: 56px;
    width: 420px;
  }
  .contact-icon {
    position: absolute;
    left: 0;
    top: 0;
  }
  .contact-colon {
    position: absolute;
    left: 62px;
    top: 4px;
    font-size: 20px;
  }
  .contact-value {
    position: absolute;
    top: 6px;
    letter-spacing: 0.5px;
    white-space: nowrap;
  }
  .contact-value--phone { left: 161px; }
  .contact-value--email { left: 99px; }
  .brand-name {
    position: absolute;
    right: 60px;
    top: 232px;
    margin: 0;
    font-size: 36px;
    font-weight: 700;
    color: var(--teal);
    white-space: nowrap;
  }
  .back-email {
    position: absolute;
    left: 0;
    right: 0;
    top: 210px;
    margin: 0;
    text-align: center;
    font-size: 42px;
    color: var(--white);
    letter-spacing: 1px;
    white-space: nowrap;
  }
  .back-brand {
    position: absolute;
    right: 40px;
    bottom: 45px;
    margin: 0;
    font-size: 24px;
    font-weight: 700;
    color: var(--faint);
    white-space: nowrap;
  }
</style>
</head>
<body>
  <section class="card card--front">
    <h1 class="holder-name">Your Name</h1>
    <p class="holder-position">Position</p>

    <ul class="contact-list">
      <li class="contact-item">
        <svg class="contact-icon" width="26" height="40" viewBox="0 0 26 40" aria-hidden="true">
          <rect x="3" y="2" width="20" height="36" rx="4" fill="none" stroke="#00c6c7" stroke-width="2"/>
          <rect x="7" y="7" width="12" height="11" fill="none" stroke="#00c6c7" stroke-width="1.5"/>
          <line x1="7" y1="23" x2="19" y2="23" stroke="#00c6c7" stroke-width="1.5"/>
          <line x1="7" y1="28" x2="19" y2="28" stroke="#00c6c7" stroke-width="1.5"/>
          <line x1="7" y1="33" x2="19" y2="33" stroke="#00c6c7" stroke-width="1.5"/>
        </svg>
        <span class="contact-colon">:</span>
        <span class="contact-value contact-value--phone">+60198765432</span>
      </li>
      <li class="contact-item">
        <svg class="contact-icon" width="30" height="36" viewBox="0 0 30 36" aria-hidden="true">
          <path d="M7 2 L11 9 L8 13 C10 19 14 24 19 27 L23 24 L28 30 L23 34 C13 31 5 20 3 7 Z" fill="none" stroke="#00c6c7" stroke-width="2" stroke-linejoin="round"/>
        </svg>
        <span class="contact-colon">:</span>
        <span class="contact-value contact-value--phone">+60198765432</span>
      </li>
      <li class="contact-item">
        <svg class="contact-icon" width="38" height="40" viewBox="0 0 38 40" aria-hidden="true">
          <rect x="2" y="10" width="34" height="22" fill="none" stroke="#00c6c7" stroke-width="2"/>
          <polyline points="2,10 19,23 36,10" fill="none" stroke="#00c6c7" stroke-width="2"/>
          <line x1="2" y1="32" x2="14" y2="20" stroke="#00c6c7" stroke-width="1.5"/>
          <line x1="36" y1="32" x2="24" y2="20" stroke="#00c6c7" stroke-width="1.5"/>
        </svg>
        <span class="contact-colon">:</span>
        <span class="contact-value contact-value--email">info@tcrest.co</span>
      </li>
    </ul>

    <p class="brand-name">Tallow Crest</p>
  </section>

  <section class="card card--back">
    <p class="back-email">hello@tcrest.co</p>
    <p class="back-brand">Tallow Crest</p>
  </section>
</body>
</html>
```